Professionelles Social Media Material für Reinigungsdienstleister
Schnelle und unkomplizierte Abwicklung - Briefing wurde nach Wünschen umgesetzt und entsprach direkt den Vorstellungen!
Zielgruppe
Wir reinigen Privathaushalte, Ferienwohnungen, Arztpraxen und Büroräume.
Aufgabenstellung
Ich wünsche Material für ein professionelles Auftreten bei Facebook und Instagram. Wir müssen bei Facebook leider neu starten und haben Instagram bei dieser Firma bisher vernachlässigt.
Nun wollen wir unser Social Media professionell erscheinen lassen und einen Plan für die kommenden 2 Monate erstellen. Wir suchen dafür mindestens 20 passende Postings und die Inhalte für den Start.
Nachtrag zu den Postings: Wir wollen ganz allgemeinen Content und sind offen für alle Vorschläge. Es kann gern auch eine Sommeraktion beworben werden, bei der wir Neukunden 100€ schenken und eine Aktion, bei der es eine kostenlose Erstreinigung gibt um unsere Leistung zu testen.

```html
<!DOCTYPE html>
<html lang="de">
<head>
<meta charset="utf-8">
<title>Putzwerk Pioniere – Sommeraktion</title>
<link rel="stylesheet" href="https://fonts.googleapis.com/css2?family=Roboto:wght@400;500;700;900&display=swap">
<style>
  :root {
    --navy: #4a5b8c;
    --teal: #3ba0c4;
    --white: #ffffff;
    --sky: #dbeef3;
    --aqua: #8fd0dc;
    --sand: #e3c48f;
    --sand-deep: #c99d5c;
    --badge-top: #3b93bd;
    --badge-bottom: #4d5f90;
  }
  * { margin: 0; padding: 0; box-sizing: border-box; }
  html, body { width: 1200px; height: 1200px; overflow: hidden; background: var(--white); }
  body { font-family: "Roboto", Arial, sans-serif; }

  .post { position: relative; width: 1200px; height: 1200px; background: var(--white); overflow: hidden; }

  .hero-photo {
    position: absolute; left: 440px; top: 0; width: 760px; height: 780px;
    background:
      linear-gradient(to right, var(--white) 0%, rgba(255,255,255,0) 28%),
      linear-gradient(to top, var(--white) 0%, rgba(255,255,255,0) 22%),
      linear-gradient(160deg, #f3f7f8 0%, var(--sky) 35%, var(--aqua) 60%, #b9d6a8 85%, #e9efe6 100%);
  }

  .supplies-photo {
    position: absolute; left: 590px; top: 790px; width: 610px; height: 410px;
    background:
      linear-gradient(to right, var(--white) 0%, rgba(255,255,255,0) 20%),
      linear-gradient(to top, var(--sand) 0%, var(--sand) 18%, rgba(227,196,143,0) 40%),
      radial-gradient(ellipse at 35% 55%, #45b7c4 0%, #7fd0d6 30%, rgba(255,255,255,0) 65%),
      var(--white);
  }

  .brand {
    position: absolute; left: 88px; top: 78px;
    display: flex; align-items: center; gap: 10px;
    color: var(--navy); font-weight: 700; font-size: 24px; line-height: 1.15;
  }
  .brand-mark { width: 22px; height: 22px; background: var(--teal); flex: none; }

  .headline {
    position: absolute; left: 84px; top: 222px;
    color: var(--navy); font-weight: 900; font-size: 121px; line-height: 103px;
    letter-spacing: -1px; text-transform: uppercase;
  }

  .subline {
    position: absolute; left: 86px; top: 676px;
    color: var(--teal); font-weight: 900; text-transform: uppercase; letter-spacing: 0;
  }
  .subline .big { display: block; font-size: 88px; line-height: 82px; }
  .subline .small { display: block; font-size: 72px; line-height: 72px; }

  .offer-text {
    position: absolute; left: 88px; top: 858px;
    color: var(--navy); font-size: 32px; font-weight: 400; line-height: 37px;
  }

  .cta {
    position: absolute; left: 88px; top: 978px; width: 398px; height: 86px;
    background: var(--navy); border-radius: 9px;
    color: var(--white); font-size: 27px; font-weight: 500;
    display: flex; align-items: center; justify-content: center;
  }

  .website {
    position: absolute; left: 88px; top: 1098px;
    color: var(--navy); font-size: 24px; font-weight: 700;
  }

  .badge {
    position: absolute; left: 892px; top: 560px; width: 246px; height: 246px;
    border-radius: 50%;
    background: linear-gradient(160deg, var(--badge-top), var(--badge-bottom));
    box-shadow: 0 0 0 4px var(--white), 0 0 0 6px var(--badge-bottom), 0 6px 16px rgba(0,0,0,0.18);
    color: var(--white); font-weight: 900; text-transform: uppercase;
    display: flex; align-items: center; justify-content: center;
  }
  .badge-text { transform: rotate(-14deg); text-align: center; line-height: 1; }
  .badge-small { display: block; font-size: 25px; font-weight: 700; }
  .badge-amount { display: block; font-size: 82px; letter-spacing: -2px; margin: 4px 0; }
  .badge-amount sup { font-size: 36px; vertical-align: 24px; margin-left: 2px; }
  .badge-label { display: block; font-size: 31px; font-weight: 700; }
</style>
</head>
<body>
  <main class="post">
    <div class="hero-photo" role="img" aria-label="Frau mit Sonnenbrille sitzt entspannt auf einem Fenstersims eines weißen Strandhauses mit hellblauen Fensterläden, dazu Palmen und Seesterne"></div>
    <div class="supplies-photo" role="img" aria-label="Türkiser Putzeimer mit Sprühflaschen, Bürsten und Tüchern auf Sand mit Seesternen und Muscheln"></div>

    <div class="brand">
      <span class="brand-mark"></span>
      <span class="brand-name">Putzwerk<br>Pioniere</span>
    </div>

    <h1 class="headline">Mehr<br>Zeit<br>für<br>Sonne</h1>

    <h2 class="subline"><span class="big">Wir machen</span><span class="small">den Rest.</span></h2>

    <p class="offer-text">Jetzt Sommerangebot sichern –<br>für ein strahlend sauberes Zuhause!</p>

    <a class="cta">Sommer-Rabatt sichern</a>

    <p class="website">putzwerkpioniere.de</p>

    <div class="badge">
      <div class="badge-text">
        <span class="badge-small">Jetzt</span>
        <span class="badge-amount">100<sup>€</sup></span>
        <span class="badge-label">Sparen!</span>
      </div>
    </div>
  </main>
</body>
</html>
```